Telecom company needs marketing flyers

We need 3 different flyers to describe our product and how to qualify for the program. This our website to use for the logo and color scheme https://www.brivolinkmobile.com, however do not use the mascot on the flyer.

Attached are examples of a competitors flyers.

```html
<!DOCTYPE html>
<html lang="en">
<head>
<meta charset="utf-8">
<title>Brivolink Mobile – Tablet Offer Flyer</title>
<link rel="stylesheet" href="https://fonts.googleapis.com/css2?family=Poppins:wght@400;500;600;700&display=swap">
<style>
  :root {
    --stage: #f3d9d9;
    --brand-blue: #0a64c6;
    --brand-blue-dark: #0753a8;
    --teal-top: #12b6d2;
    --teal-bottom: #0fc4b5;
    --paper: #ffffff;
    --highlight: #f3f7b4;
    --placeholder-dark: #1b1f2a;
    --placeholder-screen: #1466c8;
  }

  * { box-sizing: border-box; margin: 0; padding: 0; }

  html, body {
    width: 1200px;
    height: 800px;
    overflow: hidden;
  }

  body {
    background: var(--stage);
    font-family: "Poppins", sans-serif;
    position: relative;
  }

  .flyer {
    position: absolute;
    left: 300px;
    top: 15px;
    width: 600px;
    height: 770px;
    background: var(--paper);
    overflow: hidden;
    box-shadow: 0 6px 24px rgba(0, 0, 0, 0.12);
  }

  .flyer__backdrop {
    position: absolute;
    inset: 0;
  }

  .brand-disc {
    position: absolute;
    left: -2px;
    top: -101px;
    width: 202px;
    height: 202px;
    border-radius: 50%;
    background: var(--brand-blue);
  }

  .brand-name {
    position: absolute;
    left: 20px;
    top: 18px;
    color: var(--paper);
    font-weight: 500;
    line-height: 1;
    text-align: right;
  }

  .brand-name__main {
    display: block;
    font-size: 25px;
    letter-spacing: 2px;
  }

  .brand-name__sub {
    display: block;
    font-size: 8px;
    letter-spacing: 1.5px;
    margin-top: 3px;
  }

  .product-visual {
    position: absolute;
    left: 221px;
    top: 59px;
    width: 353px;
    height: 255px;
    border-radius: 10px;
    background: linear-gradient(160deg, var(--placeholder-screen), var(--brand-blue-dark));
    border: 12px solid var(--placeholder-dark);
  }

  .deal-badge {
    position: absolute;
    left: 18px;
    top: 279px;
    width: 202px;
    height: 202px;
    border-radius: 50%;
    background: var(--brand-blue);
    border: 4px solid var(--paper);
    box-shadow: 0 3px 10px rgba(0, 0, 0, 0.25);
    display: flex;
    align-items: center;
    justify-content: center;
  }

  .deal-badge__text {
    color: var(--paper);
    font-weight: 700;
    font-size: 17px;
    line-height: 1.3;
    text-align: center;
    transform: rotate(-15deg);
  }

  .offer-box {
    position: absolute;
    left: 23px;
    top: 504px;
    width: 254px;
    height: 155px;
    border-radius: 8px;
    background: var(--brand-blue);
    color: var(--paper);
    font-weight: 600;
    font-size: 21px;
    line-height: 1.32;
    text-align: center;
    display: flex;
    align-items: center;
    justify-content: center;
  }

  .offer-box__highlight { color: var(--highlight); font-weight: 700; }

  .steps__label {
    position: absolute;
    left: 332px;
    top: 452px;
    width: 225px;
    height: 28px;
    border-radius: 8px;
    background: var(--brand-blue);
    color: var(--paper);
    font-weight: 600;
    font-size: 11.5px;
    display: flex;
    align-items: center;
    justify-content: center;
  }

  .steps__rail {
    position: absolute;
    left: 324px;
    top: 520px;
    width: 1.5px;
    height: 150px;
    background: var(--brand-blue);
  }

  .step {
    position: absolute;
    left: 312px;
    display: flex;
    align-items: center;
    gap: 9px;
    color: var(--brand-blue);
    font-weight: 600;
    font-size: 15px;
    line-height: 1.15;
    white-space: nowrap;
  }

  .step__number {
    flex: none;
    width: 25px;
    height: 25px;
    background: var(--brand-blue);
    color: var(--paper);
    font-size: 14px;
    display: flex;
    align-items: center;
    justify-content: center;
  }

  .step--one   { top: 504px; }
  .step--two   { top: 557px; }
  .step--three { top: 610px; }
  .step--four  { top: 654px; }

  .footer-band {
    position: absolute;
    left: 0;
    top: 706px;
    width: 600px;
    height: 64px;
    background: var(--brand-blue);
    color: var(--paper);
  }

  .footer-band__contact,
  .footer-band__social {
    position: absolute;
    top: 8px;
    text-align: center;
  }

  .footer-band__contact { left: 55px; width: 200px; }
  .footer-band__social  { left: 315px; width: 200px; }

  .footer-band__heading {
    font-weight: 600;
    font-size: 16px;
    line-height: 1.2;
  }

  .footer-band__phone {
    font-weight: 600;
    font-size: 23px;
    line-height: 1.25;
  }

  .social-list {
    display: flex;
    justify-content: center;
    gap: 13px;
    margin-top: 6px;
    list-style: none;
  }

  .social-list__item {
    width: 25px;
    height: 25px;
    border: 1.5px solid rgba(255, 255, 255, 0.55);
    background: rgba(255, 255, 255, 0.08);
  }
</style>
</head>
<body>
  <main class="flyer">
    <svg class="flyer__backdrop" width="600" height="770" viewBox="0 0 600 770" aria-hidden="true">
      <defs>
        <linearGradient id="teal-wash" x1="0" y1="0" x2="0" y2="1">
          <stop offset="0" stop-color="var(--teal-top)"/>
          <stop offset="1" stop-color="var(--teal-bottom)"/>
        </linearGradient>
      </defs>
      <path d="M0,0 H600 V354 C380,452 120,372 0,216 Z" fill="var(--brand-blue)"/>
      <path d="M0,0 H600 V344 C380,440 120,362 0,206 Z" fill="url(#teal-wash)"/>
    </svg>

    <div class="brand-disc"></div>
    <div class="brand-name">
      <span class="brand-name__main">BRIVOLINK</span>
      <span class="brand-name__sub">MOBILE</span>
    </div>

    <div class="product-visual" role="img" aria-label="Illustration of a tablet showing a wifi signal on its screen"></div>

    <div class="deal-badge">
      <p class="deal-badge__text">GET YOUR LIMITED<br>TIME DEAL TODAY!</p>
    </div>

    <div class="offer-box">
      <p>
        <span class="offer-box__highlight">FREE SERVICE</span> AND<br>
        <span class="offer-box__highlight">INTERNET</span> WITH<br>
        YOUR <span class="offer-box__highlight">TABLET!</span>
      </p>
    </div>

    <section class="steps">
      <h2 class="steps__label">FOLLOW THESE SIMPLE STEPS</h2>
      <div class="steps__rail"></div>
      <div class="step step--one"><span class="step__number">1</span><span>Check coverage in your area</span></div>
      <div class="step step--two"><span class="step__number">2</span><span>Get in touch with us</span></div>
      <div class="step step--three"><span class="step__number">3</span><span>Pick Your Plan</span></div>
      <div class="step step--four"><span class="step__number">4</span><span>Place Order, Active<br>Your Plan, &amp; Enjoy!</span></div>
    </section>

    <footer class="footer-band">
      <div class="footer-band__contact">
        <p class="footer-band__heading">Contact Us</p>
        <p class="footer-band__phone">+8005550142</p>
      </div>
      <div class="footer-band__social">
        <p class="footer-band__heading">Follow Us</p>
        <ul class="social-list" aria-label="Social channels">
          <li class="social-list__item"></li>
          <li class="social-list__item"></li>
          <li class="social-list__item"></li>
          <li class="social-list__item"></li>
          <li class="social-list__item"></li>
        </ul>
      </div>
    </footer>
  </main>
</body>
</html>
```